Groundbreaking technology company needs packaging for its devices.

We are a new tech company based in Bakersfield, CA called 'Corvel Systems'. We have designed an innovative intelligent device, the 'Quillo', that can securely send massive amount of data in real time. Our 'Quillo' has innovative security and software that works in conjunction with the 'Corvel Cloud'.Our devices are currently sold to the oil and other energy industries. Potentially reaching into the common household.We are needing to create an exciting and effective packaging to ship our devices globally. The packaging must be able to protect the 'Quillo' and its components from moisture, static, and impact.Being we are a groundbreaking technology, we would like to create an interesting package for our customers to receive. (Packaging must be easy to assemble, exciting for the customer to open, cost effective, and use minimal materials.)Thanks for your interest,and Good Luck!

Target Market(s)

Oil and other energy industries. Potentially reaching into the common household.

Industry/Entity Type

Oil And Gas

Font styles to use
Serif

Colors

Designer to choose colors to be used in the design.

Requirements
Must have
• Packaging must protect the 'Quillo' and its components from moisture, static, and impact.
Nice to have
• Easy assemble package, exciting for the customer to open, cost effective, and use minimal materials.

```html
<!DOCTYPE html>
<html lang="en">
<head>
<meta charset="utf-8">
<title>Quillo Packaging Layout</title>
<link href="https://fonts.googleapis.com/css2?family=Arimo:wght@400;700&family=Bebas+Neue&display=swap" rel="stylesheet">
<style>
  :root{
    --navy:#25354d;
    --orange:#f36f2a;
    --charcoal:#333d45;
    --sky:#21bdec;
    --paper:#ffffff;
    --backdrop:#eeeeee;
    --ink:#ffffff;
  }
  *{margin:0;padding:0;box-sizing:border-box}
  html,body{width:1200px;height:1200px;overflow:hidden}
  body{background:var(--backdrop);font-family:"Arimo",Arial,sans-serif;position:relative}
  .sheet-title{position:absolute;left:20px;top:26px;font-family:"Bebas Neue",Impact,sans-serif;font-size:34px;letter-spacing:-0.5px;color:#111;line-height:1}
  .panel{position:absolute;left:716px;width:462px;background:var(--navy);color:var(--ink)}
  .panel--brand{top:22px;height:390px}
  .brand-band{position:absolute;left:0;top:98px;width:100%;height:170px;background:var(--paper);display:flex;align-items:center;justify-content:center;gap:14px}
  .brand-dot{width:22px;height:22px;border-radius:50%;background:var(--orange)}
  .brand-name{font-size:40px;font-weight:400;color:var(--charcoal);letter-spacing:1px}
  .brand-info{position:absolute;left:0;top:306px;width:100%;text-align:center;font-size:15px;line-height:19px}
  .panel--specs{top:441px;height:282px}
  .spec-col{position:absolute;top:60px;width:210px}
  .spec-col:first-child{left:33px}
  .spec-col:last-child{left:250px}
  .spec-title{font-size:14px;font-weight:400;color:var(--orange);margin-bottom:22px;white-space:nowrap}
  .spec-list{list-style:none;font-size:9.5px;line-height:11.1px}
  .panel--software{top:752px;height:391px}
  .software-copy{position:absolute;left:35px;top:130px;width:205px}
  .software-title{font-size:17px;font-weight:400;color:var(--orange);margin-bottom:14px}
  .software-text{font-size:11.3px;line-height:13.6px}
  .feature-list{position:absolute;left:274px;top:122px;list-style:none}
  .feature{display:flex;align-items:center;gap:14px;height:42px;margin-bottom:9px;font-size:11px}
  .feature-icon{width:42px;height:42px;border-radius:7px;background:var(--paper);display:flex;align-items:center;justify-content:center}
  .swatch{position:absolute;width:69px;height:69px}
  .swatch--orange{left:525px;top:586px;background:var(--orange)}
  .swatch--navy{left:550px;top:562px;background:var(--navy)}
  .swatch--sky{left:579px;top:537px;background:var(--sky)}
  .swatch--white{left:606px;top:510px;background:var(--paper)}
  .panel--front{position:absolute;left:65px;top:721px;width:583px;height:421px;background:var(--orange);overflow:hidden}
  .brush-area{position:absolute;left:70px;top:20px;width:560px;height:380px;background:linear-gradient(160deg,#ffffff 55%,#fde8dc 100%);transform:rotate(-22deg);border-radius:40px;opacity:.97}
  .front-mark{position:absolute;left:0;top:0;width:100%;height:100%;display:flex;flex-direction:column;align-items:center;justify-content:center;gap:18px}
  .front-square{width:90px;height:90px;background:var(--charcoal)}
  .front-name{font-size:46px;font-weight:700;color:var(--charcoal);letter-spacing:2px}
</style>
</head>
<body>
  <h1 class="sheet-title">Product Packaging Layout</h1>

  <div class="swatch swatch--orange"></div>
  <div class="swatch swatch--navy"></div>
  <div class="swatch swatch--sky"></div>
  <div class="swatch swatch--white"></div>

  <section class="panel--front">
    <div class="brush-area" role="img" aria-label="White painted brush stroke sweeping across the orange panel"></div>
    <div class="front-mark">
      <div class="front-square"></div>
      <div class="front-name">QUILLO</div>
    </div>
  </section>

  <section class="panel panel--brand">
    <div class="brand-band">
      <span class="brand-dot"></span>
      <span class="brand-name">Corvel Systems</span>
    </div>
    <p class="brand-info">For more Information<br>Please visit us at www.corvelsystems.com</p>
  </section>

  <section class="panel panel--specs">
    <div class="spec-col">
      <h2 class="spec-title">QUILLO SPECIFICATIONS</h2>
      <ul class="spec-list">
        <li>4 analog inputs</li><li>10 discrete inputs</li><li>5 discrete outputs</li><li>3G cellular</li><li>Wireless 802.11</li><li>GPS</li><li>Industrial ethernet</li><li>USB</li><li>Bluetooth</li><li>SMS texting for alarms</li><li>12-30 VDC input</li>
      </ul>
    </div>
    <div class="spec-col">
      <h2 class="spec-title">THE QUILLO FEATURES</h2>
      <ul class="spec-list">
        <li>4 analog inputs</li><li>10 discrete inputs</li><li>5 discrete outputs</li><li>3G cellular</li><li>Wireless 802.11</li><li>GPS</li><li>Industrial ethernet</li><li>USB</li><li>Bluetooth</li><li>SMS texting for alarms</li><li>12-30 VDC input</li>
      </ul>
    </div>
  </section>

  <section class="panel panel--software">
    <div class="software-copy">
      <h2 class="software-title">THE SOFTWARE</h2>
      <p class="software-text">The Quillo firmware is a custom, highly secure, Linux-based operating system that is capable of receiving over-the air (OTA) updates. Backwards compatible updates, security upgrades, and enhancements are automatically rolled out and deployed.</p>
    </div>
    <ul class="feature-list">
      <li class="feature">
        <span class="feature-icon"><svg width="30" height="22" viewBox="0 0 30 22"><path d="M8 19h15a5 5 0 0 0 0-10 7 7 0 0 0-13-2A5.5 5.5 0 0 0 8 19z" fill="none" stroke="#21bdec" stroke-width="2"/><path d="M11 16l4-5 3 3 4-5" fill="none" stroke="#25354d" stroke-width="1.6"/></svg></span>
        fast data transfer.
      </li>
      <li class="feature">
        <span class="feature-icon"><svg width="24" height="28" viewBox="0 0 24 28"><path d="M12 1l10 4v8c0 7-5 11-10 14C7 24 2 20 2 13V5z" fill="#21bdec"/><path d="M7 14l4 4 7-8" fill="none" stroke="#25354d" stroke-width="2.4"/></svg></span>
        secure connection.
      </li>
      <li class="feature">
        <span class="feature-icon"><svg width="24" height="26" viewBox="0 0 24 26"><path d="M4 2l18 11L4 24z" fill="#21bdec"/></svg></span>
        plug and play.
      </li>
    </ul>
  </section>
</body>
</html>
```